Packaging design for high end, natural skin care line needed

Marisol Thackery Beauty needs a label design. It is a new skin care line I am launching.
For years my line Velvet Orchard Beauty was quite popular and featured in several magazines, but for personal reasons had to be shut down. Now I am launching a new line featuring VOB's top selling products, but focused solely on skin care more so than cosmetics. All products will still be handmade, but the line should still look professional-something worthy of a Brindle Market shelf!
I am branding it with my name, as I am often quoted in articles related to gluten in beauty products, so Marisol Thackery and beauty are key words.
The key products will be facial and body serums which are packaged in .5oz., 1oz. and larger amber glass bottles with black dropper tops, I will include pictures below. For dimensions, the labels can be any size that you think will work best, but need to at the least fit the 1oz. bottle, dimensions shown here http://www.corvelflask.example/amber-glass-tall-round-flask/p/QZ7K-93/
I loved the former VOB logo, but for Marisol Thackery Beauty I am looking for something more personal, more apothecary-like, and probably less colorful.
The line will be small, just a handful of products, but luxe, rich.
I am attaching photos of Velvet Orchard Beauty's packaging for your reference.
Thanks much!!

Hi Everyone! Thank you for your submissions! Please see the links I provided in the brief, I really am looking for something more technical looking, like an apothecary. And want black text on a white background, not a black background, and nothing flowery.
Thank you all!!
Marisol

Target Market(s)

My clients are primarily women of all ages, but with more of a skin care focus, and no longer a cosmetic one, I would also like to appeal to a male audience. My clients are health conscious, gluten-free, natural, paleo, or vegan, etc. Target age is probably 25-55. Products are a bit high end, priced $45-65.

Industry/Entity Type

Cosmetics

Requirements
Must have
• It must at least say Marisol Thackery, or can say Marisol Thackery Beauty, but "Beauty" is not necessary. And capitalization is open, try whatever you think serves the brand. Likely slogans or taglines that can be included but are not essential: Care for your skin. Love and care for your skin. Handmade with love in the USA. Handmade in the USA. Think modern day apothecary. Small batch scotch. Something fine, but custom, handmade.
Nice to have
• I like the aesthetic of Oribel Skin Care a bit http://www.oribelhollis.example.au/
And of Dorian Valtz as shown here http://www.pinboardia.example/pin/847302915563017442/
Also of something like this that is even customizable http://www.pinboardia.example/pin/58274106392285514/
Every product is handmade in small batches, with fine ingredients, a moderate price point of around $45-$65. And I will likely begin making custom orders. So there could be a space to say when it was made, or for whom. I would like to keep the colors classic though, I probably want to stay away from the bright pink on this one.
Should not have
• As I mentioned, probably want to stay away from a lot of color. I like black vs. gray for the text, as it will show up better in editorials. I must look good, but also photograph well. Thanks!

```html
<!DOCTYPE html>
<html lang="en">
<head>
<meta charset="utf-8">
<title>Marisol Thackery – Body Serum Labels</title>
<link rel="stylesheet" href="https://fonts.googleapis.com/css2?family=Share+Tech+Mono&display=swap">
<style>
  :root {
    --paper: #ffffff;
    --label-ground: #ffffff;
    --label-edge: #111111;
    --ink: #111111;
    --band-stone: #e4e1dc;
    --band-sage: #dfe6df;
    --band-sand: #ece5d8;
    --band-moss: #e3e5d6;
  }
  html, body {
    margin: 0;
    padding: 0;
    width: 690px;
    height: 1200px;
    overflow: hidden;
    background: var(--paper);
  }
  .label-sheet {
    position: relative;
    width: 690px;
    height: 1200px;
    font-family: "Share Tech Mono", monospace;
    color: var(--ink);
  }
  .label {
    position: absolute;
    left: 0;
    width: 689px;
    height: 262px;
    box-sizing: border-box;
    border: 1px solid var(--label-edge);
    background: var(--label-ground);
    text-align: center;
  }
  .label p, .label h2 { margin: 0; font-weight: 400; }
  .label--stone { top: 0; --band: var(--band-stone); }
  .label--sage { top: 298px; --band: var(--band-sage); }
  .label--sand { top: 619px; --band: var(--band-sand); }
  .label--moss { top: 937px; height: 263px; --band: var(--band-moss); }

  .tagline {
    position: absolute;
    top: 10px;
    left: 0;
    right: 0;
    font-size: 12px;
    letter-spacing: 2.2px;
    line-height: 16px;
  }
  .brand-band {
    position: absolute;
    top: 35px;
    left: 0;
    right: 0;
    height: 63px;
    background: var(--band);
    border-top: 1px solid var(--label-edge);
    border-bottom: 1px solid var(--label-edge);
  }
  .brand-mark {
    position: absolute;
    top: 11px;
    left: 50%;
    width: 12px;
    height: 12px;
    margin-left: -6px;
    border: 1.5px solid var(--ink);
    border-radius: 50%;
    box-sizing: border-box;
  }
  .brand-name {
    position: absolute;
    top: 38px;
    left: 0;
    right: 0;
    font-size: 15px;
    letter-spacing: 1.3px;
    line-height: 18px;
  }
  .product-name {
    position: absolute;
    top: 114px;
    left: 0;
    right: 0;
    font-size: 18px;
    letter-spacing: 4.3px;
    line-height: 22px;
    -webkit-text-stroke: 0.4px var(--ink);
  }
  .fill-line {
    position: absolute;
    left: 272px;
    width: 142px;
    height: 0;
    border-bottom: 1px dotted var(--ink);
  }
  .fill-line--made { top: 189px; }
  .fill-line--for { top: 213px; }
  .volume {
    position: absolute;
    top: 234px;
    left: 0;
    right: 0;
    font-size: 18px;
    letter-spacing: 1.8px;
    line-height: 20px;
    -webkit-text-stroke: 0.3px var(--ink);
  }
</style>
</head>
<body>
<main class="label-sheet">
  <section class="label label--stone">
    <p class="tagline">CARE FOR YOUR SKIN</p>
    <div class="brand-band"><span class="brand-mark"></span><p class="brand-name">Marisol Thackery</p></div>
    <h2 class="product-name">BODY SERUM</h2>
    <span class="fill-line fill-line--made"></span>
    <span class="fill-line fill-line--for"></span>
    <p class="volume">1oz</p>
  </section>

  <section class="label label--sage">
    <p class="tagline">CARE FOR YOUR SKIN</p>
    <div class="brand-band"><span class="brand-mark"></span><p class="brand-name">Marisol Thackery</p></div>
    <h2 class="product-name">BODY SERUM</h2>
    <span class="fill-line fill-line--made"></span>
    <span class="fill-line fill-line--for"></span>
    <p class="volume">1oz</p>
  </section>

  <section class="label label--sand">
    <p class="tagline">CARE FOR YOUR SKIN</p>
    <div class="brand-band"><span class="brand-mark"></span><p class="brand-name">Marisol Thackery</p></div>
    <h2 class="product-name">BODY SERUM</h2>
    <span class="fill-line fill-line--made"></span>
    <span class="fill-line fill-line--for"></span>
    <p class="volume">1oz</p>
  </section>

  <section class="label label--moss">
    <p class="tagline">CARE FOR YOUR SKIN</p>
    <div class="brand-band"><span class="brand-mark"></span><p class="brand-name">Marisol Thackery</p></div>
    <h2 class="product-name">BODY SERUM</h2>
    <span class="fill-line fill-line--made"></span>
    <span class="fill-line fill-line--for"></span>
    <p class="volume">1oz</p>
  </section>
</main>
</body>
</html>
```